Banner ad for hyper local news site

We need a banner (that we will use on our own site) to explain to people that they can "be the reporter" in their local area. Lanternpost is an Australia community news network. We cover local news on a daily basis but also allow people and organisations to publish their own news direct to the site. We are trying to encourage local dialogue and to empower people to talk about the things that matter to them and get their issues on the news agenda.

We need a 'call to action' banner that explains to our users that they can post their own stories on the site.

Some suggested text (thinking this would be rolling)

*Lanternpost is YOUR voice in the community
*You can 'be the reporter' and write your own news
*To be heard, contribute your stories, click here - it's free

The banner doesn't have to be slick - we'd prefer a warm and friendly community feeling....but also something in keeping with the look and feel of our site wwww.lanternpost-example.com.au

Industry/Entity Type

News

```html
<!DOCTYPE html>
<html lang="en">
<head>
<meta charset="utf-8">
<title>Lanternpost – Be the Reporter banner frames</title>
<link rel="stylesheet" href="https://fonts.googleapis.com/css2?family=Arimo:wght@400;700&display=swap">
<style>
  :root {
    --page-bg: #ffffff;
    --label-ink: #111111;
    --frame-edge: #3a3a3a;
    --banner-bg-top: #f7f7f7;
    --banner-bg-bottom: #e6e6e6;
    --brand-blue: #1b8ad6;
    --panel-green-top: #3fb24a;
    --panel-green-mid: #249a34;
    --panel-green-bottom: #1d8a2c;
    --panel-edge: #15701f;
    --message-ink: #ffffff;
    --cta-ink: #ffec1a;
    --photo-dark: #2c3a2e;
    --photo-mid: #6e7b70;
    --photo-light: #b9c2bb;
  }
  * { box-sizing: border-box; margin: 0; padding: 0; }
  html, body {
    width: 1200px;
    height: 614px;
    overflow: hidden;
    background: var(--page-bg);
    font-family: "Arimo", Arial, sans-serif;
  }
  .storyboard {
    position: relative;
    width: 1200px;
    height: 614px;
  }
  .frame-row {
    position: absolute;
    left: 0;
    width: 1200px;
    height: 107px;
  }
  .frame-row.first { top: 103px; }
  .frame-row.second { top: 257px; }
  .frame-row.third { top: 410px; }
  .frame-label {
    position: absolute;
    left: 80px;
    top: 36px;
    font-size: 30px;
    line-height: 1;
    color: var(--label-ink);
  }
  .banner {
    position: absolute;
    left: 234px;
    top: 0;
    width: 866px;
    height: 107px;
    border: 2px solid var(--frame-edge);
    background: linear-gradient(var(--banner-bg-top), var(--banner-bg-bottom));
    overflow: hidden;
  }
  .brand {
    position: absolute;
    left: 0;
    top: 0;
    width: 172px;
    height: 103px;
    display: flex;
    align-items: center;
    justify-content: center;
    gap: 6px;
  }
  .brand-dot {
    width: 14px;
    height: 14px;
    border-radius: 50%;
    background: var(--brand-blue);
    flex: none;
  }
  .brand-name {
    font-weight: 700;
    font-size: 25px;
    color: var(--brand-blue);
    letter-spacing: -0.5px;
  }
  .message-panel {
    position: absolute;
    left: 174px;
    top: 8px;
    width: 680px;
    height: 89px;
    border: 1px solid var(--panel-edge);
    border-radius: 8px 0 0 8px;
    background: linear-gradient(var(--panel-green-top), var(--panel-green-mid) 45%, var(--panel-green-bottom));
    overflow: hidden;
  }
  .message {
    position: absolute;
    left: 0;
    top: 0;
    width: 474px;
    height: 87px;
    display: flex;
    flex-direction: column;
    align-items: center;
    justify-content: center;
    color: var(--message-ink);
    font-size: 29px;
    line-height: 36px;
    text-align: center;
    white-space: nowrap;
  }
  .message .cta {
    color: var(--cta-ink);
    font-weight: 700;
  }
  .presenter-photo {
    position: absolute;
    right: 0;
    top: -8px;
    width: 212px;
    height: 105px;
    background: linear-gradient(90deg, var(--photo-light) 0%, var(--photo-mid) 40%, var(--photo-dark) 100%);
  }
</style>
</head>
<body>
<main class="storyboard">

  <section class="frame-row first">
    <p class="frame-label">Frame 1</p>
    <div class="banner">
      <div class="brand"><span class="brand-dot"></span><span class="brand-name">Lanternpost</span></div>
      <div class="message-panel">
        <p class="message"><span>Lanternpost is YOUR voice</span><span>in the community</span></p>
      </div>
      <div class="presenter-photo" role="img" aria-label="Photo of a smiling presenter wearing a headset beside a computer monitor"></div>
    </div>
  </section>

  <section class="frame-row second">
    <p class="frame-label">Frame 2</p>
    <div class="banner">
      <div class="brand"><span class="brand-dot"></span><span class="brand-name">Lanternpost</span></div>
      <div class="message-panel">
        <p class="message"><span>You can 'be the reporter'</span><span>and write your own news</span></p>
      </div>
      <div class="presenter-photo" role="img" aria-label="Photo of a smiling presenter wearing a headset beside a computer monitor"></div>
    </div>
  </section>

  <section class="frame-row third">
    <p class="frame-label">Frame 3</p>
    <div class="banner">
      <div class="brand"><span class="brand-dot"></span><span class="brand-name">Lanternpost</span></div>
      <div class="message-panel">
        <p class="message"><span>To be heard, contribute your stories,</span><span class="cta">click here - it's free</span></p>
      </div>
      <div class="presenter-photo" role="img" aria-label="Photo of a smiling presenter wearing a headset beside a computer monitor"></div>
    </div>
  </section>

</main>
</body>
</html>
```